Newly opened kids play space needs brochure to show what our space has to offer

Tri-fold color brochure with same aethetic as website (www.fernhollowplayhouse.com) that provides a comprehensive and visual overview of what our play space is comprised of. Features of the brochure should include our logo, "A Garrick and Pellinger-inspired Play Space in the Poconos", photos of: Dedicated Infant Play Area; Cafe and Free WiFi; Weekly Themed Activities; Unique Classes; Parties and Events. Photos also of our open play area with children playing within it. Info within the brochure should include our location, hours. Please take some copy from : https://www.facebook.com/fernhollowtinkerplayhouse/?ref=bookmarks
and from the Plan Your Visit part of the website. I have a lot of photos to use; is there a way to put in generic photo placeholders and I can pick which photos of mine to go into the various areas of the brochure, or if you need the photos ahead of time, please let me know the best way to proceed. I am attaching the logo files for now.

Font styles to use
Sans Serif

Colors
85cae6
cee9f5
86cfc6
cfeae6
fdf9cf
fff3d1
eaf2ce
cadf82

Requirements
Must have
• Eye catching placement of photos; color scheme similar to website and logo colors
Should not have
• Brochure should be simple, not too colorful - no primary colors, not too crowded.

```html
<!DOCTYPE html>
<html lang="en">
<head>
<meta charset="utf-8">
<title>Fern Hollow Play Space – Brochure Inside Spread</title>
<link rel="stylesheet" href="https://fonts.googleapis.com/css2?family=Open+Sans:ital,wght@1,800&family=Tenor+Sans&family=Encode+Sans+Semi+Condensed:wght@600&display=swap">
<style>
  :root {
    --page-bg: #f1f1ef;
    --panel-grey: #e2e2da;
    --panel-cream: #fbf8d6;
    --story-brown: #5a2e1c;
    --ink: #3d3a35;
    --ink-soft: #4a4740;
    --blue: #2a9fd0;
    --green: #6fb85a;
    --salmon: #e07b5f;
    --purple: #9b7bc4;
    --teal: #3bb9b0;
    --sky: #85cae6;
    --mint: #86cfc6;
    --lime: #cadf82;
    --circle: rgba(134, 207, 198, 0.18);
  }
  * { box-sizing: border-box; margin: 0; padding: 0; }
  html, body { width: 1200px; height: 1048px; overflow: hidden; background: var(--page-bg); }
  .spread { position: relative; width: 1200px; height: 1048px; }

  .panel { position: absolute; top: 0; height: 1048px; width: 400px; overflow: hidden; }
  .panel--photos { left: 0; background: var(--panel-grey); }
  .panel--story { left: 400px; background: var(--panel-cream); }
  .panel--features { left: 800px; background: var(--panel-grey); }

  .photo { position: absolute; border-radius: 3px; }

  .tagline-box {
    position: absolute; left: 12px; top: 16px; width: 196px; height: 170px;
    border-radius: 8px;
    background: linear-gradient(135deg, #2a8fb8 0%, #4fa5a0 55%, #8cc35a 100%);
    display: flex; flex-direction: column; justify-content: center; padding-left: 30px;
  }
  .tagline-box span {
    font-family: "Open Sans", sans-serif; font-weight: 800; font-style: italic;
    font-size: 40px; line-height: 42px; color: #e8eef0; letter-spacing: 1px;
    text-shadow: 1px 2px 2px rgba(0,0,0,0.35);
  }

  .band-rule {
    position: absolute; left: 12px; top: 664px; width: 600px; height: 12px;
    background: linear-gradient(90deg, #2a8fb8, #4fa5a0 50%, #8cc35a);
  }
  .swatches { position: absolute; left: 612px; top: 664px; display: flex; gap: 3px; }
  .swatches i { display: block; width: 12px; height: 12px; }

  .circle-deco {
    position: absolute; left: 540px; top: 420px; width: 440px; height: 440px;
    border-radius: 50%; background: var(--circle);
  }

  .story { position: absolute; left: 430px; top: 38px; width: 345px; color: var(--ink); }
  .story h2 {
    font-family: "Encode Sans Semi Condensed", sans-serif; font-weight: 600;
    font-size: 30px; color: var(--story-brown); text-align: center;
  }
  .story .rule {
    width: 120px; height: 1px; background: #b9a88a; margin: 6px auto 24px;
  }
  .story p {
    font-family: "Tenor Sans", sans-serif; font-size: 15px; line-height: 21px;
    text-align: justify; margin-bottom: 18px;
  }
  .story blockquote {
    font-family: "Tenor Sans", sans-serif; font-size: 17px; color: #1f1d1a;
    margin-top: 6px;
  }

  .feature { position: absolute; left: 812px; width: 198px; }
  .feature h3 {
    font-family: "Tenor Sans", sans-serif; font-weight: 400; font-size: 14px;
    color: #2f2c28; padding-left: 7px; border-left: 4px solid var(--accent);
    line-height: 18px; margin-bottom: 12px; letter-spacing: -0.2px;
  }
  .feature p {
    font-family: "Tenor Sans", sans-serif; font-size: 13.5px; line-height: 20px;
    color: var(--ink-soft); text-align: justify; padding-left: 10px;
  }
  .feature-photo {
    position: absolute; left: 1022px; width: 164px; height: 172px;
    border-radius: 3px; border-bottom: 4px solid var(--accent);
  }
</style>
</head>
<body>
<main class="spread">

  <section class="panel panel--photos">
    <div class="tagline-box"><span>PLAY</span><span>LEARN</span><span>GROW</span></div>
    <div class="photo" style="left:214px;top:16px;width:178px;height:170px;background:linear-gradient(135deg,#b88a6a,#8a7b9a);" role="img" aria-label="Photo: children sitting in a circle on a round rug with teachers"></div>
    <div class="photo" style="left:12px;top:192px;width:190px;height:462px;background:linear-gradient(180deg,#6f9fbf,#5a7d94 50%,#8a5a55);" role="img" aria-label="Photo: play corner with pink blossoms, stars and a wooden toy kitchen"></div>
    <div class="photo" style="left:208px;top:192px;width:184px;height:170px;background:linear-gradient(135deg,#8ab39a,#a07a78);" role="img" aria-label="Photo: children doing crafts around a table"></div>
    <div class="photo" style="left:208px;top:368px;width:184px;height:286px;background:linear-gradient(180deg,#6f7a4f,#9a8770 60%,#c9a9b8);" role="img" aria-label="Photo: smiling girl sitting on branches in the woods"></div>
  </section>

  <section class="panel panel--story"></section>

  <section class="panel panel--features"></section>

  <div class="circle-deco" aria-hidden="true"></div>

  <div class="band-rule" aria-hidden="true"></div>
  <div class="swatches" aria-hidden="true">
    <i style="background:#2a8fb8"></i><i style="background:#85cae6"></i><i style="background:#9b7bc4"></i><i style="background:#e07b9f"></i><i style="background:#86cfc6"></i><i style="background:#cadf82"></i><i style="background:#6fb85a"></i><i style="background:#e8b35a"></i><i style="background:#e07b5f"></i><i style="background:#b8a8d8"></i>
  </div>

  <div class="photo" style="left:12px;top:684px;width:776px;height:350px;background:linear-gradient(90deg,#b58a6e,#a47a62 40%,#8f9a7a 75%,#b98a70);" role="img" aria-label="Photo: open play area with children playing on the wooden floor"></div>

  <article class="story">
    <h2>Our Story</h2>
    <div class="rule"></div>
    <p>Fern Hollow was born out of a desire for a different kind of play space in the Poconos. A play space that celebrates the quieter, natural curiosities of the child.</p>
    <p>In our rushed daily lives filled with noise, electronics, and running on overdrive, Fern Hollow is a place that brings us down a notch and let’s us simply, play.</p>
    <p>Combining Garrick and Pellinger philosophies in the materials and activities we have thoughtfully selected to introduce at Fern Hollow, our play space provides an open-ended, multi-sensory approach to play, nourishing the whole child. We have a range of classes for all ages, and are happy to host your next party or event as well.</p>
    <p>Catch up on work with our free Wi-Fi or simply relax in our cafe while having a Brewline, tea, simple healthy snacks or a cold beverage.</p>
    <blockquote>“We look forward to welcoming you to Fern Hollow”</blockquote>
  </article>

  <div class="feature" style="top:62px;--accent:var(--blue)">
    <h3>Dedicated Infant Play Area</h3>
    <p>Bond safely with your baby while being within eyeshot of the main play area.</p>
  </div>
  <div class="feature-photo" style="top:34px;--accent:var(--blue);background:linear-gradient(135deg,#c9b8a8,#6a7a8f);" role="img" aria-label="Photo: parent with baby in the infant play area"></div>

  <div class="feature" style="top:262px;--accent:var(--green)">
    <h3>Cafe and Free WiFi</h3>
    <p>Take a break or catch up on work while enjoying Brewline coffee, beverages, and snacks.</p>
  </div>
  <div class="feature-photo" style="top:234px;--accent:var(--green);background:linear-gradient(135deg,#8a8f9a,#a67e62);" role="img" aria-label="Photo: parent enjoying coffee at a cafe table"></div>

  <div class="feature" style="top:462px;--accent:var(--salmon)">
    <h3>Weekly Themed Activities</h3>
    <p>Stories, crafts, and activities change weekly to celebrate the seasons and the world around us.</p>
  </div>
  <div class="feature-photo" style="top:434px;--accent:var(--salmon);background:linear-gradient(135deg,#a9b4c0,#c9a86a);" role="img" aria-label="Photo: children with flower crowns at a craft table"></div>

  <div class="feature" style="top:662px;--accent:var(--purple)">
    <h3>Unique Classes</h3>
    <p>Our multi-age, multi-sensory approach to traditional classes nurtures the whole child in a creative and fun way.</p>
  </div>
  <div class="feature-photo" style="top:634px;--accent:var(--purple);background:linear-gradient(135deg,#8fa0a8,#b88a5a);" role="img" aria-label="Photo: children and parents dancing during a class"></div>

  <div class="feature" style="top:862px;--accent:var(--teal)">
    <h3>Parties and Events</h3>
    <p>Forget a stress, have a fun and enjoy with kids in delightfully conducted events and parties.</p>
  </div>
  <div class="feature-photo" style="top:834px;--accent:var(--teal);background:linear-gradient(135deg,#b9a8a0,#6aa8b0);" role="img" aria-label="Photo: kids playing games on mats at a party"></div>

</main>
</body>
</html>
```